■書籍タイトル
「町工房・路地の店・士業のための、明日効く集客設計術・KRT」

・堅苦しくなく、わかりやすいイメージにしたいです
・電子書籍なので、画像が小さいので、できるだけ視認しやすい文字でお願いします

■オビ
「お金も時間もかけずに、たった2つのことをするだけで、ライバルが歯ぎしりするほどお客に選ばれる」

■著者  森野沙知絵
■発行  東陽商務文化出版舎

■色の指定などはありません。お任せです。
(明るい・カンタン・わかりやすい)
イメージイラストなど入ってもよいかと思います。

■高級感やアカデミックより、明るくカンタンなイメージで。

※参考資料として、書籍の原稿と、同じタイトルのセミナーのパワポ表紙画像を添付します。
アカデミックな感じより、ポップな感じや明るいイメージ、
「わかりやすさ」「文字の視認性」を重視します。
クラフターのみなさま、
引き続き、ご提案をお待ちしております。
みなさま、ご提案ありがとうございます。

中小企業・小さなお店・先生業
という文字が小さい表示のデザインが多いのですが、

ターゲット層が一目で見てわかるよう、

中小企業・小さなお店・先生業

という文字が見えるようにしたいです。

引き続き、みなさまからのご提案をお待ちしております。
たくさんのご提案をいただきありがとうございます。

本のタイトルが、変更となりました。
金額をアップし、締め切りを1日延長いたしますので、
訂正ご対応いただければ幸いです。

新しいタイトルは、

「中小企業・小さなお店・先生業が
常連が増え続けるために明日から始める三つの習慣」
です。

帯、またはサブタイトルは、
「ライバルが歯ぎしりするほどお客が押し寄せる新時代の差別化戦略」
としてください。

ご提案をお待ちしております。
よろしくお願いいたします。

今回の装丁は、特に「わかりやすさ」を重視しておりました。
レベルの高い装丁デザインが多く、選考に大変迷いました。
選定させていただきましたデザインは、笑顔の3職種の人物のイラストと、フォントの使い方など、わかりやすい・明るい・カンタンという目指すところをこちらの想定以上に表現していただいたことが一番の理由です。

たくさんのご提案をいただき、ありがとうございました。
本当にレベルの高いデザインが多く選定では社内でも意見が割れました。
また、再三の追記・変更によりお手数をおかけしましたことを、この場を借りてお詫び申し上げます。

今後も定期的に装丁の依頼をいたしますので、どうぞよろしくお願いいたします。

```html
<!DOCTYPE html>
<html lang="ja">
<head>
<meta charset="utf-8">
<title>町工房・路地の店・士業が常連が増え続けるために明日から始める三つの習慣</title>
<link rel="stylesheet" href="https://fonts.googleapis.com/css2?family=Noto+Sans+JP:wght@400;700;900&family=Noto+Serif+JP:wght@600&display=swap">
<style>
  :root {
    --paper: #ffffff;
    --frame: #d9d9d9;
    --ink: #1a1a1a;
    --red: #e60012;
    --green: #1e9a3c;
    --orange: #ef7d00;
    --navy: #1d3f8a;
    --figure-a: #f6c9a0;
    --figure-b: #9cc3e6;
  }
  * { margin: 0; padding: 0; box-sizing: border-box; }
  html, body { width: 750px; height: 1200px; overflow: hidden; background: var(--paper); }
  body { font-family: "Noto Sans JP", sans-serif; color: var(--ink); }

  .cover { position: relative; width: 750px; height: 1200px; border: 2px solid var(--frame); overflow: hidden; }

  .v { position: absolute; writing-mode: vertical-rl; font-weight: 900; line-height: 1; white-space: nowrap; }

  /* target badge */
  .target-badge { position: absolute; left: 332px; top: 0; width: 360px; height: 330px; }
  .target-badge__text {
    position: absolute; left: 382px; top: 92px; width: 260px;
    text-align: center; color: #fff; font-weight: 900; font-size: 44px; line-height: 1.22;
  }

  /* title */
  .title-action { left: 247px; top: 75px; font-size: 66px; }
  .title-count { left: 92px; top: 75px; }
  .title-count__num { font-size: 116px; color: var(--red); }
  .title-count__rest { font-size: 100px; }

  .title-reason__a { left: 636px; top: 312px; font-size: 54px; color: var(--red); }
  .title-reason__b { left: 529px; top: 337px; font-size: 50px; color: var(--green); }
  .title-reason__c { left: 424px; top: 337px; font-size: 52px; color: var(--red); }

  /* author */
  .author { position: absolute; left: 212px; top: 700px; width: 250px; text-align: center; }
  .author__name { font-family: "Noto Serif JP", serif; font-weight: 600; font-size: 40px; letter-spacing: 0.1em; line-height: 1.2; }
  .author__roman { font-family: "Noto Serif JP", serif; font-size: 19px; font-style: italic; color: #555; }

  /* obi */
  .obi { position: absolute; left: 510px; top: 608px; width: 228px; height: 400px; border: 4px solid var(--orange); }
  .obi__rival { left: 686px; top: 622px; font-size: 28px; }
  .obi__crowd { left: 604px; top: 622px; font-size: 46px; color: var(--orange); }
  .obi__method { left: 534px; top: 622px; }
  .obi__method-lead { font-size: 30px; }
  .obi__method-key { font-size: 44px; color: var(--orange); }

  /* pitch */
  .pitch { position: absolute; left: 112px; top: 785px; width: 400px; }
  .pitch__lead { font-size: 27px; font-weight: 700; color: var(--orange); }
  .pitch__headline { font-size: 38px; font-weight: 900; color: var(--navy); line-height: 1.22; margin-top: 4px; }
  .pitch__detail { font-size: 19px; font-weight: 700; line-height: 1.6; margin-top: 14px; }

  .figure {
    position: absolute; left: 562px; top: 1010px; width: 150px; height: 170px;
    border-radius: 75px 75px 12px 12px;
    background: linear-gradient(180deg, var(--figure-a) 0%, var(--figure-b) 70%);
  }

  .publisher { position: absolute; left: 112px; top: 1140px; font-size: 21px; font-weight: 700; }
</style>
</head>
<body>
<main class="cover">
  <svg class="target-badge" viewBox="0 0 360 330" aria-hidden="true">
    <defs><path id="badge-arc" d="M22 172 A158 158 0 0 1 338 172"/></defs>
    <circle cx="180" cy="168" r="140" fill="var(--red)"/>
    <text font-family="Noto Sans JP, sans-serif" font-weight="700" font-size="19" fill="var(--ink)">
      <textPath href="#badge-arc" startOffset="50%" text-anchor="middle">あなたの人生のターニングポイントに!</textPath>
    </text>
  </svg>
  <p class="target-badge__text">町工房<br>路地の店<br>士業が</p>

  <h1>
    <span class="v title-reason__a">常連が</span>
    <span class="v title-reason__b">増え続ける</span>
    <span class="v title-reason__c">ために</span>
    <span class="v title-action">明日から始める</span>
    <span class="v title-count"><span class="title-count__num">三つ</span><span class="title-count__rest">の習慣</span></span>
  </h1>

  <div class="author">
    <p class="author__name">森野 沙知絵</p>
    <p class="author__roman">sachie morino</p>
  </div>

  <aside>
    <div class="obi"></div>
    <p class="v obi__rival">ライバルが歯ぎしりするほど</p>
    <p class="v obi__crowd">お客が押し寄せる</p>
    <p class="v obi__method"><span class="obi__method-lead">明日効く</span><span class="obi__method-key">集客設計術</span></p>
  </aside>

  <section class="pitch">
    <p class="pitch__lead">ライバルと圧倒的に差がつく。</p>
    <p class="pitch__headline">規模の小さな会社ほど<br>有利な方法!</p>
    <p class="pitch__detail">町工房、路地の店、飲食店などの店主や<br>税理士、行政書士など士業の方<br>などがKRTを習得し、実践中!</p>
  </section>

  <div class="figure" role="img" aria-label="笑顔で親指を立てるスーツ姿の男性のイラスト"></div>

  <p class="publisher">東陽商務文化出版舎</p>
</main>
</body>
</html>
```